Custom Framing Shop Tallpine Framing Studio

I want an eye catching graphic that will be used a s business sign on a busy road. The sign MUST communicate the type of business it is clearly to vehicles traveling at 40 mph. This is a custom picture framing business and the sign will be hanging and be approximately 32" X 48". The business name is Tallpine Framing Studio; Custom framing: by appointment and should include a whole or partial image of a picture frame as a visual que. I've included inspiration idea's, color pallets and styles that I like and a current business card for inspiration. I like the crimson font style shadowing and background colors of the attached Olans pizzeria sign. I'd prefer crimson letters. Custom Framing is the message to communicate, followed by phone number and business name. I like the idea of a shield shape with a banner since it would more eye catching, Once again the Tallpine image and name is less important than communicating what the business does. I like Crimson, grey, gold, black but am open to new ideas . I like the idea of a shield with a banner more than a rectangle, but am open to idea's

Target Market(s)

My target market is local homeowners ($700k+) who want a relationship with their framer and are willing to pay for a customized experience compared to a craft store experience. I have more female clients then men.

Industry/Entity Type

Picture Framing Art

Other font styles liked:
• Look at the attached image of a custom pizzeria sign, its kid of a custom car pinstripe font style. Script and decorative may be difficult to read while driving by but add to the elegance.

Colors

Designer to choose colors to be used in the design.

Requirements
Must have
• Clearly communicate what the business does "Custom framing" preferably with a picture frame and words
Nice to have
• incorporate a Tallpine into the graphic
Should not have
• A Tallpine image doesn't communicate what the business does to a vehicle traveling at 40 mph by the sign

```html
<!DOCTYPE html>
<html lang="en">
<head>
<meta charset="utf-8">
<title>Tallpine Framing Studio – Custom Framing Sign</title>
<link rel="stylesheet" href="https://fonts.googleapis.com/css2?family=Crimson+Pro:wght@700&family=Rubik:wght@700;800&display=swap">
<style>
  :root {
    --page: #ffffff;
    --panel: #f3ddb8;
    --crimson: #a31f24;
    --gold: #b8771f;
    --gold-shadow: #cdab80;
    --ink: #231815;
  }
  html, body {
    margin: 0;
    padding: 0;
    width: 1200px;
    height: 768px;
    overflow: hidden;
    background: var(--page);
  }
  .sign {
    display: block;
    width: 1200px;
    height: 768px;
  }
  .sign__panel { fill: var(--panel); }
  .sign__border { fill: none; stroke: var(--crimson); stroke-width: 8; }
  .brand__mark { fill: var(--crimson); }
  .brand__name {
    font-family: "Rubik", sans-serif;
    font-weight: 700;
    font-size: 30px;
    fill: var(--ink);
  }
  .headline {
    font-family: "Crimson Pro", serif;
    font-weight: 700;
    font-size: 128px;
  }
  .headline--shadow { fill: var(--gold-shadow); }
  .headline--main { fill: var(--gold); }
  .services__box {
    fill: none;
    stroke: var(--gold);
    stroke-width: 1.5;
  }
  .services__item {
    font-family: "Rubik", sans-serif;
    font-weight: 800;
    font-size: 40px;
    fill: var(--ink);
  }
  .services__dot { fill: var(--gold); }
  .phone {
    font-family: "Rubik", sans-serif;
    font-weight: 800;
    font-size: 86px;
    fill: var(--crimson);
  }
</style>
</head>
<body>
<svg class="sign" viewBox="0 0 1200 768" xmlns="http://www.w3.org/2000/svg" role="img" aria-label="Tallpine Framing Studio custom framing sign">
  <rect class="sign__panel" x="145" y="81" width="910" height="606"/>
  <path class="sign__border" d="M176,93 H1026 A18,18 0 0 0 1044,111 V659 A18,18 0 0 0 1026,677 H176 A18,18 0 0 0 158,659 V111 A18,18 0 0 0 176,93 Z"/>

  <g class="brand">
    <rect class="brand__mark" x="454" y="169" width="16" height="16"/>
    <text class="brand__name" x="484" y="190">Tallpine Framing Studio</text>
  </g>

  <text class="headline headline--shadow" x="184" y="337" textLength="840" lengthAdjust="spacingAndGlyphs">Custom Framing</text>
  <text class="headline headline--main" x="180" y="332" textLength="840" lengthAdjust="spacingAndGlyphs">Custom Framing</text>

  <g class="services">
    <rect class="services__box" x="340" y="358" width="520" height="179" rx="3"/>
    <circle class="services__dot" cx="480" cy="394" r="5"/>
    <text class="services__item" x="600" y="410" text-anchor="middle">FRAMING</text>
    <circle class="services__dot" cx="720" cy="394" r="5"/>

    <circle class="services__dot" cx="419" cy="444" r="5"/>
    <text class="services__item" x="600" y="460" text-anchor="middle">SHADOW BOXES</text>
    <circle class="services__dot" cx="781" cy="444" r="5"/>

    <circle class="services__dot" cx="366" cy="501" r="5"/>
    <text class="services__item" x="600" y="517" text-anchor="middle" textLength="428" lengthAdjust="spacingAndGlyphs">VETERAN FLAG CASES</text>
    <circle class="services__dot" cx="834" cy="501" r="5"/>
  </g>

  <text class="phone" x="297" y="642" textLength="600" lengthAdjust="spacingAndGlyphs">(360) 555 – 0148</text>
</svg>
</body>
</html>
```